GroovePulse918 - Internet Radio Station Needs a Website

Site Description:
Groovepulse918 is an Internet radio station feed that broadcasts Groove Pulse 918 hours per day, 7 days per week. The stream is hosted by Tarnivo.example, a BeamRelay partner. Groovepulse918 has various programming schedules and an Auto DJ program is enabled when there is no live programming. There are several DJs that provide content for programming, and Groovepulse918 also does live pop-up events at various venues. Currently, there is no front-end design, if you visit groovepulse918.example or groovepulse918-radio.example, each domain URL is pointed to the default BeamRelay player and feed that is hosted by Tarnivo. The goal is to create a front-end design and website that will be optimized for mobile devices, as most of the streaming will be to mobile devices; the site should be responsive.

Here are some templates that offer similar functionality:
https://www.layoutharbor.example/demo/40372.html
https://www.layoutharbor.example/demo/61835.html

LOGO and Aesthetics:
From an aesthetic standpoint, house music is a very underground, New York-centric genre of music. I have uploaded an image that mirrors the New York Subway signage motif. I like the underground feel and "grittyness" of the subway. I want to make sure that the "2", "4", and "7" images in their respective circles and colors (red, green, and purple) are utilized in any logo design, these subway lines are highly recognizable and I want to play off that familiarity because everyone in New York City can identify with them (the fonts and colors would need to remain as depicted in the attachment). I need a logo that can fit into a square (or circle) so that it can be used for social media profiles; I am not opposed to the abbreviation "GP918" or some configuration whereby the "House Music" is above the (larger) "2 4 7". I have also included a picture of an electronic board that New York trains have which shows upcoming stops; possibly a navigation bar or site template might follow a similar motif.

Site Requirements:

- Text Message (SMS) API integration. I do plan on developing a mobile app, complete with push notification capabilities; however, I’d like to know whether sending SMS messages is possible in the interim, even if a subscription to a third-party service is required.

- Social Media Integration. At a minimum, users should be able to connect via Chatterbox, Chirply, and Snapgrid. I’d like to be able to incorporate the Chatterbox Live capabilities if a Chatterbox page is integrated.

- Content Management System (CMS). I need to be able to update content easily, particularly the Events calendar, Schedule, and Archives (regularly upload mp3 files/podcasts). Perhaps this means that the site needs to be a PageForge site.

- LIVE Button. I would like to “activate” a LIVE button and possible scrolling message or other text (on the Home Page) to correspond to live shows and events.

Site Design:
Initially, there will be six (6) pages/sections, based on the following site navigation buttons:

HOME / DJs & SHOWS / SCHEDULE / EVENTS / BLOG / IN THE MIX

- HOME: the landing page would enable anyone, registered or not, to simply click on the listen button and tune in. There would also be featured charts and playlists that would change from week to week. Users would be given the option to register and sign-in for the “premium” experience (subscribing to shows, viewing song info, access to the archives for an offline experience). All social media integration would appear on the Home Page (and probably every other page as well)

- DJs & SHOWS: DJ bios and show descriptions would be provided, along with contact information and social media links for individual DJs. Downloadable press kits for each DJ would be available here, and a “Book Me” (contact form) email form as well.

- SCHEDULE: this would be a calendar showing daily programming and upcoming shows (by month)

- EVENTS: this would show upcoming events, complete with any flyer artwork and Wayfinder Maps integration (API). Maybe even Chatterbox event integration (who’s going, etc)

- BLOG: blog section complete with the ability to upload videos, audio, and images to associate with the written content

- IN THE MIX: this section will have archives of DJ mixes and shows, for offline listening. Registered users would have access to this section so that they can download any of the archived mixes for offline listening. The mixes would be indexed but should also be searchable by DJ or keyword.

Target Market(s)

18-40, people who frequently go out to bars, clubs, lounges

Industry/Entity Type

Radio Station

Logo Text

"Groove Pulse 918" or "GP918"

Coding

Coded - Design and coding required

Font styles to use
Sans Serif

Requirements
Must have
• - Optimized for mobile (Responsive)
• - Pull stream from Tarnivo/BeamRelay server, a “LISTEN NOW” button should prominently appear on the Home page. Once a listener clicks on the button, the audio should stream on the same page (without a new page having to be opened). If a listener wishes to navigate throughout the site, a pop-up window should appear with the player controls. There are various BeamRelay-compatible players that can be embedded in the site, or there should be a way to link a button to the actual stream destination (http://s1.tarnivo.example:8808/index.html OR http://station.tarnivo.example/3c91e2d07a5fb/)
• - Sign In/Register option. Non-registered users can listen, but will not have access to all areas of the site. Once signed in, a user would have access to all areas of the site (including archived mixes/podcasts). Registration would require a name, email address, possible Chatterbox sign-in, and a mobile device number (optional). Signed in users would be able to ‘Like’, ‘Share’, ‘Chirp’, etc. and possibly even create their own playlists.
Nice to have
• - Text Message (SMS) API integration. I do plan on developing a mobile app, complete with push notification capabilities; however, I’d like to know whether sending SMS messages is possible in the interim, even if a subscription to a third-party service is required.
• - LIVE Button. I would like to “activate” a LIVE button and possible scrolling message or other text (on the Home Page) to correspond to live shows and events.

```html
<!DOCTYPE html>
<html lang="en">
<head>
<meta charset="utf-8">
<title>Groove Pulse 918 — Internet Radio</title>
<link rel="stylesheet" href="https://fonts.googleapis.com/css2?family=Roboto+Condensed:wght@400;700&family=Open+Sans:wght@400;600&display=swap">
<style>
:root{
  --red:#d9222e;
  --green:#179b4a;
  --magenta:#c2479f;
  --sky:#0f9edc;
  --ink:#333;
  --muted:#666;
  --line:#e2e2e2;
  --footer:#f2f2f2;
  --white:#fff;
  --head:"Roboto Condensed",sans-serif;
  --body:"Open Sans",sans-serif;
}
*{margin:0;padding:0;box-sizing:border-box}
html,body{width:1200px;height:2782px;overflow:hidden;background:var(--white)}
body{font-family:var(--body);color:var(--ink);position:relative}

/* hero */
.hero{position:absolute;left:0;top:0;width:1200px;height:642px;
  background:linear-gradient(100deg,#3a2620 0%,#6a3a2a 30%,#8b5a42 55%,#4a2d26 80%,#2c1e1d 100%)}
.hero-shade{position:absolute;inset:0;background:linear-gradient(90deg,rgba(0,0,0,.45),rgba(0,0,0,.1) 60%,rgba(0,0,0,.25))}
.brand{position:absolute;left:98px;top:45px;display:flex;align-items:center;gap:12px;
  font-family:var(--head);font-weight:700;font-size:30px;color:var(--white)}
.brand-dot{width:22px;height:22px;border-radius:50%;background:var(--red)}
.account{position:absolute;top:52px;right:100px;display:flex;gap:12px}
.btn-sm{font-family:var(--head);font-size:13px;color:var(--white);padding:8px 14px;border-radius:3px;text-transform:uppercase}
.btn-register{background:var(--green)}
.btn-signin{border:1px solid var(--white)}
.nav{position:absolute;top:108px;right:100px;display:flex;gap:36px;font-family:var(--head);font-size:14px;color:var(--white);text-transform:uppercase}
.hero-title{position:absolute;left:98px;top:268px;font-family:var(--head);font-weight:700;font-size:50px;color:var(--white);text-transform:uppercase}
.hero-copy{position:absolute;left:98px;top:338px;width:380px;font-size:13.5px;line-height:22px;color:var(--white)}
.btn-live{position:absolute;left:98px;top:395px;width:126px;height:36px;background:var(--green);border:1px solid #7fd39d;
  color:var(--white);font-family:var(--head);font-size:14px;display:flex;align-items:center;justify-content:center;gap:6px}
.dots{position:absolute;left:100px;top:450px;display:flex;gap:8px;align-items:center}
.dots span{width:10px;height:10px;border-radius:50%;background:var(--white)}
.dots span.on{width:16px;height:16px;border:3px solid var(--white);background:transparent;box-shadow:inset 0 0 0 2px #555}

/* features */
.features{position:absolute;left:98px;top:642px;width:1003px;height:235px;display:flex}
.feature{flex:1;position:relative;color:var(--white);text-align:center;padding-top:88px}
.feature-red{background:var(--red)}
.feature-green{background:var(--green)}
.feature-magenta{background:var(--magenta)}
.feature-icon{position:absolute;left:50%;top:-37px;width:104px;height:104px;margin-left:-52px;border-radius:50%;background:var(--white);
  display:flex;align-items:center;justify-content:center;border:4px solid rgba(255,255,255,.6)}
.feature h3{font-family:var(--head);font-weight:400;font-size:20px;text-transform:uppercase;margin-bottom:10px}
.feature p{font-size:11px;line-height:20px;padding:0 24px}
.feature .more{display:inline-block;margin-top:14px;font-family:var(--head);font-size:12.5px;text-transform:uppercase}

/* welcome */
.welcome{position:absolute;left:165px;top:962px;width:870px;text-align:center}
.welcome h2{font-family:var(--head);font-weight:400;font-size:33px;color:#3a3a3a;text-transform:uppercase;margin-bottom:16px}
.welcome p{font-size:10.5px;line-height:20px;color:var(--muted)}
.btn-outline{display:inline-block;margin-top:20px;border:1px solid #999;padding:5px 9px;font-family:var(--head);font-size:11px;color:#333;text-transform:uppercase}

/* shows */
.shows{position:absolute;left:0;top:1208px;width:1200px;height:546px;
  background:radial-gradient(ellipse at 50% 10%,#4a2e5a 0%,#231a32 40%,#0d0b14 100%)}
.shows h2{position:absolute;top:57px;width:100%;text-align:center;font-family:var(--head);font-weight:400;font-size:31px;color:var(--white);text-transform:uppercase}
.show-card{position:absolute;top:139px;width:239px;height:279px;background:var(--white);text-align:center}
.show-photo{height:160px}
.show-card h4{font-family:var(--body);font-weight:400;font-size:15.5px;margin:15px 0 8px;color:#222}
.show-card p{font-size:11.5px;line-height:19px;color:var(--muted);padding:0 14px}
.shows-curve{position:absolute;left:0;bottom:-1px}

/* news & charts */
.section-title{font-family:var(--head);font-weight:400;font-size:25px;color:#333;text-transform:uppercase}
.news{position:absolute;left:98px;top:1803px;width:635px}
.news-item{position:absolute;left:0;width:635px;height:170px;border-bottom:1px solid var(--line)}
.news-photo{position:absolute;left:0;top:0;width:215px;height:141px}
.news-body{position:absolute;left:238px;top:0;width:397px}
.news-body h4{font-family:var(--body);font-weight:400;font-size:15px;color:#333;margin-bottom:12px}
.news-date{font-size:11.5px;font-style:italic;color:#1a3f9c;margin-bottom:10px}
.news-body p{font-size:11.5px;line-height:20px;color:var(--muted)}
.charts{position:absolute;left:810px;top:1803px;width:300px}
.chart-list{list-style:none;margin-top:30px}
.chart-list li{display:flex;align-items:center;gap:12px;height:30.8px;font-size:12px;color:#333}

/* social band */
.social-band{position:absolute;left:0;top:2289px;width:1200px;height:148px;background:var(--sky);color:var(--white)}
.social-badge{position:absolute;left:169px;top:24px;width:92px;height:92px;border-radius:50%;background:#1b72b8;box-shadow:0 2px 4px rgba(0,0,0,.25)}
.social-text{position:absolute;left:293px;top:22px;width:790px;font-size:11px;line-height:20px}
.social-text .tag{font-size:12px;margin-top:4px}
.social-text .link{font-weight:600;font-size:11px}

/* footer */
.footer{position:absolute;left:0;top:2437px;width:1200px;height:286px;background:var(--footer)}
.footer-col{position:absolute;top:50px}
.footer h5{font-family:var(--head);font-weight:400;font-size:17px;color:#333;text-transform:uppercase;margin-bottom:12px}
.footer p,.footer li{font-size:11.5px;line-height:19px;color:#444}
.footer-brand{display:flex;align-items:center;gap:8px;font-family:var(--head);font-weight:700;font-size:22px;color:#222;margin-bottom:18px}
.footer-brand .brand-dot{width:16px;height:16px}
.social-row{display:flex;gap:7px;margin-top:14px}
.social-row span{width:23px;height:23px;border-radius:50%;border:1px solid #555}
.email-field{width:244px;height:40px;border:1px solid #ccc;background:var(--white);font-size:11px;color:#666;padding:12px 10px;margin-top:18px}
.btn-subscribe{display:inline-block;margin-top:12px;background:var(--green);color:var(--white);font-family:var(--head);font-size:13px;padding:9px 16px;text-transform:uppercase}
.contact-row{display:flex;gap:14px;margin-bottom:12px}
.contact-row svg{flex:none;margin-top:3px}
.quick-links{list-style:none}
.quick-links li{display:flex;align-items:center;gap:9px;font-size:11px;line-height:20.5px}
.quick-links li::before{content:"";border-left:5px solid #444;border-top:4px solid transparent;border-bottom:4px solid transparent}
.copyright{position:absolute;left:0;top:2723px;width:1200px;height:59px;border-top:1px solid #ddd;text-align:center;font-size:11.5px;line-height:56px;color:#333}
</style>
</head>
<body>

<header class="hero" role="img" aria-label="Photo of a smiling listener with a phone and headphones in a warm-lit studio">
  <div class="hero-shade"></div>
  <div class="brand"><span class="brand-dot"></span>Groove Pulse 918</div>
  <div class="account">
    <span class="btn-sm btn-register">Register</span>
    <span class="btn-sm btn-signin">Sign-In</span>
  </div>
  <nav class="nav">
    <span>Home</span><span>DJs &amp; Shows</span><span>Schedule</span><span>Events</span><span>Blog</span><span>In The Mix</span>
  </nav>
  <h1 class="hero-title">Groove Pulse 918</h1>
  <p class="hero-copy">Sed ut perspiciatis unde omnis iste natus error sit voluptatem accusantium doloremque laudantium, totam</p>
  <span class="btn-live">LISTEN LIVE
    <svg width="12" height="12" viewBox="0 0 12 12"><path d="M4 2v6.5a1.8 1.8 0 1 1-1-1.6V3.5l6-1.5v5.5a1.8 1.8 0 1 1-1-1.6V1.5z" fill="#fff"/></svg>
  </span>
  <div class="dots"><span class="on"></span><span></span><span></span><span></span></div>
</header>

<section class="features">
  <div class="feature feature-red">
    <div class="feature-icon"><svg width="48" height="48" viewBox="0 0 48 48"><path d="M18 8l22-5v27a6 6 0 1 1-4-5.6V12l-14 3v20a6 6 0 1 1-4-5.6z" fill="var(--red)"/></svg></div>
    <h3>Listen for free</h3>
    <p>Sed ut perspiciatis unde omnis iste natus error sit voluptatem accusantium doloremque laudantium, totam rem aperiam, eaque ipsa quae</p>
    <span class="more">Read more ➜</span>
  </div>
  <div class="feature feature-green">
    <div class="feature-icon"><svg width="48" height="48" viewBox="0 0 48 48"><rect x="17" y="4" width="14" height="26" rx="7" fill="var(--green)"/><path d="M11 22a13 13 0 0 0 26 0M24 35v8M17 43h14" stroke="var(--green)" stroke-width="3" fill="none"/></svg></div>
    <h3>Start your station</h3>
    <p>Sed ut perspiciatis unde omnis iste natus error sit voluptatem accusantium doloremque laudantium, totam rem aperiam, eaque ipsa quae</p>
    <span class="more">Read more ➜</span>
  </div>
  <div class="feature feature-magenta">
    <div class="feature-icon"><svg width="48" height="48" viewBox="0 0 48 48"><path d="M7 30V24a17 17 0 0 1 34 0v6" stroke="var(--magenta)" stroke-width="4" fill="none"/><rect x="6" y="27" width="10" height="15" rx="3" fill="var(--magenta)"/><rect x="32" y="27" width="10" height="15" rx="3" fill="var(--magenta)"/></svg></div>
    <h3>Listen without ads</h3>
    <p>Sed ut perspiciatis unde omnis iste natus error sit voluptatem accusantium doloremque laudantium, totam rem aperiam, eaque ipsa quae</p>
    <span class="more">Read more ➜</span>
  </div>
</section>

<section class="welcome">
  <h2>Welcome to Groove Pulse 918</h2>
  <p>Sed ut perspiciatis unde omnis iste natus error sit voluptatem accusantium doloremque laudantium, totam rem aperiam, eaque ipsa quae ab illo inventore veritatis et quasi architecto beatae vitae dicta sunt explicabo. Nemo enim ipsam voluptatem quia voluptas sit aspernatur aut odit aut fugit, sed quia consequuntur magni dolores eos qui ratione voluptatem sequi nesciunt. Neque porro quisquam est, qui dolorem ipsum quia dolor sit amet, consectetur</p>
  <span class="btn-outline">Read more ⊙</span>
</section>

<section class="shows" role="img" aria-label="Dim photo of a crowd at a club night under purple stage lights">
  <h2>Our Shows</h2>
  <article class="show-card" style="left:98px">
    <div class="show-photo" role="img" aria-label="Photo of a DJ at a studio desk" style="background:linear-gradient(135deg,#6f7d86,#2f3a40)"></div>
    <h4>Nemo enim ipsam volupt</h4>
    <p>Mauris vel lacus vitae felis vestibulum volutpat imperdiet ac nisl Cum sociis natoque sodales velit</p>
  </article>
  <article class="show-card" style="left:353px">
    <div class="show-photo" role="img" aria-label="Photo of a host with headphones and a tablet" style="background:linear-gradient(135deg,#e8e6e2,#8a7a70)"></div>
    <h4>Nemo enim ipsam volupt</h4>
    <p>Mauris vel lacus vitae felis vestibulum volutpat imperdiet ac nisl Cum sociis natoque sodales velit</p>
  </article>
  <article class="show-card" style="left:608px">
    <div class="show-photo" role="img" aria-label="Photo of a presenter at a microphone in a broadcast booth" style="background:linear-gradient(135deg,#3fb3b0,#1f4d5a)"></div>
    <h4>Nemo enim ipsam volupt</h4>
    <p>Mauris vel lacus vitae felis vestibulum volutpat imperdiet ac nisl Cum sociis natoque sodales velit</p>
  </article>
  <article class="show-card" style="left:862px">
    <div class="show-photo" role="img" aria-label="Photo of a host reading notes at a studio microphone" style="background:linear-gradient(135deg,#d9d2d6,#7a3048)"></div>
    <h4>Nemo enim ipsam volupt</h4>
    <p>Mauris vel lacus vitae felis vestibulum volutpat imperdiet ac nisl Cum sociis natoque sodales velit</p>
  </article>
  <svg class="shows-curve" width="1200" height="60" viewBox="0 0 1200 60"><path d="M0 60 Q600 -40 1200 60 Z" fill="#fff"/></svg>
</section>

<section class="news">
  <h3 class="section-title">Latest News</h3>
  <article class="news-item" style="top:65px">
    <div class="news-photo" role="img" aria-label="Photo of a singer with headphones at a studio microphone" style="background:linear-gradient(135deg,#8e8f95,#2a2b30)"></div>
    <div class="news-body">
      <h4>Sed ut perspiciatis unde omnis iste natus</h4>
      <div class="news-date">JAN 15, 2017</div>
      <p>Sed ut perspiciatis unde omnis iste natus error sit voluptatem accusantium doloremque laudantium, totam rem aperiam, eaque ipsa quae ab illo inventore veritatis et quasi architecto</p>
    </div>
  </article>
  <article class="news-item" style="top:245px">
    <div class="news-photo" role="img" aria-label="Photo of a stage microphone with colourful blurred lights" style="background:linear-gradient(135deg,#3a8fb0,#c0a030 50%,#8a2a5a)"></div>
    <div class="news-body">
      <h4>Sed ut perspiciatis unde omnis iste natus</h4>
      <div class="news-date">JAN 15, 2017</div>
      <p>Sed ut perspiciatis unde omnis iste natus error sit voluptatem accusantium doloremque laudantium, totam rem aperiam, eaque ipsa quae ab illo inventore veritatis et quasi architecto</p>
    </div>
  </article>
</section>

<section class="charts">
  <h3 class="section-title">Featured Charts</h3>
  <ul class="chart-list">
    <li><svg width="10" height="12" viewBox="0 0 10 12"><path d="M3 1l6-1v8a2 2 0 1 1-1.2-1.8V2.5L4.2 3.2V10A2 2 0 1 1 3 8.2z" fill="var(--red)"/></svg>Ellis Carrow — Crystal Line</li>
    <li><svg width="10" height="12" viewBox="0 0 10 12"><path d="M3 1l6-1v8a2 2 0 1 1-1.2-1.8V2.5L4.2 3.2V10A2 2 0 1 1 3 8.2z" fill="var(--red)"/></svg>Ellis Carrow — Wandering In My Head</li>
    <li><svg width="10" height="12" viewBox="0 0 10 12"><path d="M3 1l6-1v8a2 2 0 1 1-1.2-1.8V2.5L4.2 3.2V10A2 2 0 1 1 3 8.2z" fill="var(--red)"/></svg>Sterling Ray Vance — Prairie Rain</li>
    <li><svg width="10" height="12" viewBox="0 0 10 12"><path d="M3 1l6-1v8a2 2 0 1 1-1.2-1.8V2.5L4.2 3.2V10A2 2 0 1 1 3 8.2z" fill="var(--red)"/></svg>Fenwick Lane — I Found Another Groove</li>
    <li><svg width="10" height="12" viewBox="0 0 10 12"><path d="M3 1l6-1v8a2 2 0 1 1-1.2-1.8V2.5L4.2 3.2V10A2 2 0 1 1 3 8.2z" fill="var(--red)"/></svg>Sterling Ray Vance — Pulse and Glow</li>
    <li><svg width="10" height="12" viewBox="0 0 10 12"><path d="M3 1l6-1v8a2 2 0 1 1-1.2-1.8V2.5L4.2 3.2V10A2 2 0 1 1 3 8.2z" fill="var(--red)"/></svg>Benny Gale — Playing With The Beat</li>
    <li><svg width="10" height="12" viewBox="0 0 10 12"><path d="M3 1l6-1v8a2 2 0 1 1-1.2-1.8V2.5L4.2 3.2V10A2 2 0 1 1 3 8.2z" fill="var(--red)"/></svg>D.D. Kent &amp; Ellis Carrow — The Night Is Long</li>
    <li><svg width="10" height="12" viewBox="0 0 10 12"><path d="M3 1l6-1v8a2 2 0 1 1-1.2-1.8V2.5L4.2 3.2V10A2 2 0 1 1 3 8.2z" fill="var(--red)"/></svg>Roland Jessup — Sweet Home Harbor</li>
    <li><svg width="10" height="12" viewBox="0 0 10 12"><path d="M3 1l6-1v8a2 2 0 1 1-1.2-1.8V2.5L4.2 3.2V10A2 2 0 1 1 3 8.2z" fill="var(--red)"/></svg>Gavin Moss — Cloudy Tuesday</li>
    <li><svg width="10" height="12" viewBox="0 0 10 12"><path d="M3 1l6-1v8a2 2 0 1 1-1.2-1.8V2.5L4.2 3.2V10A2 2 0 1 1 3 8.2z" fill="var(--red)"/></svg>Fenwick Lane — I Found Another Groove</li>
    <li><svg width="10" height="12" viewBox="0 0 10 12"><path d="M3 1l6-1v8a2 2 0 1 1-1.2-1.8V2.5L4.2 3.2V10A2 2 0 1 1 3 8.2z" fill="var(--red)"/></svg>Sterling Ray Vance — Pulse and Glow</li>
  </ul>
</section>

<section class="social-band">
  <div class="social-badge"></div>
  <div class="social-text">
    <p>Lorem ipsum dolor sit amet, consectetur adipiscing elit, sed do eiusmod tempor incididunt ut labore et dolore magna aliqua. Ut enim ad minim veniam, quis nostrud exercitation ullamco laboris nisi ut aliquip ex ea commodo consequat. Duis aute irure dolor in reprehenderit in voluptate velit</p>
    <p class="tag"># Esse cillum dolore eu fugiat nulla pariatur</p>
    <p class="link">See more here http://chirp.example/k4Rb7Qx2</p>
  </div>
</section>

<footer class="footer">
  <div class="footer-col" style="left:98px;width:230px;top:48px">
    <div class="footer-brand"><span class="brand-dot"></span>Groove Pulse 918</div>
    <p>Nemo enim ipsam voluptatem quia voluptas sit aspernatur aut odit aut fugit, sed quia consequuntur magni dolores</p>
    <div class="social-row"><span></span><span></span><span></span><span></span></div>
  </div>
  <div class="footer-col" style="left:397px;width:270px">
    <h5>Sign up for newsletter</h5>
    <p>Excepteur sint occaecat cupidatat non proident, sunt in culpa qui officia deserunt</p>
    <div class="email-field">Enter email</div>
    <span class="btn-subscribe">Subscription</span>
  </div>
  <div class="footer-col" style="left:718px;width:260px">
    <h5>Contact us</h5>
    <div class="contact-row">
      <svg width="12" height="16" viewBox="0 0 12 16"><path d="M6 0a6 6 0 0 0-6 6c0 4.5 6 10 6 10s6-5.5 6-10a6 6 0 0 0-6-6zm0 8.5A2.5 2.5 0 1 1 6 3.5a2.5 2.5 0 0 1 0 5z" fill="#555"/></svg>
      <p>Groove Pulse 918<br>4410 KL Veldhaven ZH<br>The Netherlands</p>
    </div>
    <div class="contact-row">
      <svg width="13" height="13" viewBox="0 0 13 13"><path d="M2.6 0l2.2 2.8-1.3 1.6a8 8 0 0 0 5.1 5.1l1.6-1.3L13 10.4 11.4 13C5.2 13 0 7.8 0 1.6z" fill="#555"/></svg>
      <p>Phone:&nbsp; 070-555 01 42</p>
    </div>
    <div class="contact-row">
      <svg width="13" height="10" viewBox="0 0 13 10"><path d="M0 0h13v10H0zM0 0l6.5 5.5L13 0" fill="#555" stroke="#f2f2f2" stroke-width="1"/></svg>
      <p>Email: info@groovepulse918.example</p>
    </div>
  </div>
  <div class="footer-col" style="left:1011px;width:110px">
    <h5>Quick Links</h5>
    <ul class="quick-links">
      <li>About GP918</li><li>DJs &amp; Shows</li><li>Schedule</li><li>Events</li><li>Blog</li><li>Contact Us</li><li>In The Mix</li>
    </ul>
  </div>
</footer>

<div class="copyright">©2017 Groove Pulse 918 . All Rights Reserved.</div>

</body>
</html>
```